Financial firm simple design

Classic business card design for a financial fund. 2 sided card- white on both sides.. One with just the company name centered and the other w the info. info included on that is :

Name
Company position
phone number
fax
email
website

Industry/Entity Type

Financial

```html
<!DOCTYPE html>
<html lang="en">
<head>
<meta charset="utf-8">
<title>Alder Investments – Business Card</title>
<link rel="stylesheet" href="https://fonts.googleapis.com/css2?family=Open+Sans:wght@400;600&display=swap">
<style>
  :root {
    --navy: #1a4579;
    --ink: #1b1b1b;
    --muted: #555b63;
    --paper: #ffffff;
    --backdrop: #e9eaec;
  }
  * { box-sizing: border-box; margin: 0; padding: 0; }
  html, body {
    width: 1200px;
    height: 900px;
    overflow: hidden;
    background: var(--backdrop);
  }
  .canvas {
    position: relative;
    width: 1200px;
    height: 900px;
  }
  .card {
    position: absolute;
    left: 320px;
    width: 560px;
    height: 320px;
    box-shadow: 0 6px 18px rgba(0,0,0,0.18);
    overflow: hidden;
  }
  .card--front { top: 90px; background: var(--navy); }
  .card--back  { top: 490px; background: var(--paper); }

  .wordmark {
    font-family: "Open Sans", Arial, sans-serif;
    font-weight: 400;
    letter-spacing: 0.02em;
    white-space: nowrap;
    line-height: 1;
  }
  .card--front .wordmark {
    position: absolute;
    left: 0; right: 0;
    top: 140px;
    text-align: center;
    color: var(--paper);
    font-size: 34px;
  }
  .card--front .website {
    position: absolute;
    right: 36px;
    bottom: 26px;
    color: var(--paper);
    font-family: "Open Sans", Arial, sans-serif;
    font-size: 12px;
    letter-spacing: 0.14em;
  }

  .card--back .wordmark {
    position: absolute;
    left: 40px;
    top: 50px;
    color: var(--navy);
    font-size: 28px;
  }
  .contact-marker {
    position: absolute;
    left: 0;
    top: 150px;
    width: 14px;
    height: 34px;
    background: var(--navy);
  }
  .holder {
    position: absolute;
    left: 40px;
    top: 146px;
    font-family: "Open Sans", Arial, sans-serif;
  }
  .holder__name {
    color: var(--navy);
    font-size: 19px;
    font-weight: 400;
    line-height: 1.1;
  }
  .holder__role {
    color: var(--muted);
    font-size: 12px;
    margin-top: 2px;
  }
  .contact-list {
    position: absolute;
    left: 40px;
    top: 196px;
    list-style: none;
    font-family: "Open Sans", Arial, sans-serif;
    font-size: 13px;
    color: var(--muted);
    line-height: 19px;
  }
  .contact-list__label {
    color: var(--navy);
    font-weight: 600;
    display: inline-block;
    width: 12px;
  }
  .band-rule--blue {
    position: absolute;
    left: 0; right: 0;
    top: 264px;
    height: 4px;
    background: var(--navy);
  }
  .band-rule--black {
    position: absolute;
    left: 0; right: 0;
    top: 271px;
    height: 2px;
    background: var(--ink);
  }
  .footer-band {
    position: absolute;
    left: 0; right: 0;
    top: 280px;
    bottom: 0;
    background: var(--navy);
    display: flex;
    align-items: center;
    justify-content: center;
  }
  .footer-band .website {
    color: var(--paper);
    font-family: "Open Sans", Arial, sans-serif;
    font-size: 12px;
    letter-spacing: 0.16em;
  }
</style>
</head>
<body>
<main class="canvas">
  <section class="card card--front" aria-label="Card front">
    <h1 class="wordmark">Alder Investments</h1>
    <p class="website">www.alderinvestments.com</p>
  </section>

  <section class="card card--back" aria-label="Card back">
    <h2 class="wordmark">Alder Investments</h2>
    <span class="contact-marker"></span>
    <div class="holder">
      <p class="holder__name">John Doe</p>
      <p class="holder__role">Manager</p>
    </div>
    <ul class="contact-list">
      <li><span class="contact-list__label">P</span> : 555 014 208</li>
      <li><span class="contact-list__label">F</span> : 555 014 209</li>
      <li><span class="contact-list__label">E</span> : info@alderinvestments.com</li>
    </ul>
    <span class="band-rule--blue"></span>
    <span class="band-rule--black"></span>
    <div class="footer-band">
      <p class="website">www.alderinvestments.com</p>
    </div>
  </section>
</main>
</body>
</html>
```